2020 Binder Cover

Binder Design (front, spine, back) for a data analysis report in the education field. We provide a large binder full of in depth analyzed data. Design should mesh well with our 2020 report color pallet which is attached. The cover should allow for the title to be changed per Client. There is a cover example attached to give a better idea. The cover will be used with all of our clients with the name of their school district being changed for their specific report. The cover should communicate data and informed strategy for improvement and growth.

```html
<!DOCTYPE html>
<html lang="en">
<head>
<meta charset="utf-8">
<title>2020 Binder Cover – Linden School District</title>
<link href="https://fonts.googleapis.com/css2?family=Montserrat:wght@300;400;600;800&display=swap" rel="stylesheet">
<style>
  :root{
    --stage:#aaa24a;
    --paper:#ffffff;
    --ink:#2f3a3e;
    --ink-soft:#5d6a6e;
    --teal:#3c8c88;
    --mint:#8fd4c3;
    --yellow:#f4d94b;
    --coral:#ee7d6c;
    --pink:#f3a4a2;
    --peach:#f8c79f;
    --sky:#6fa8d0;
  }
  *{box-sizing:border-box;margin:0;padding:0}
  html,body{width:849px;height:1200px;overflow:hidden}
  body{background:var(--stage);font-family:"Montserrat",Arial,sans-serif;color:var(--ink);position:relative}

  .pattern{
    position:absolute;inset:0;
    background:
      linear-gradient(135deg,var(--mint) 0%,var(--yellow) 22%,var(--pink) 40%,var(--teal) 58%,var(--peach) 76%,var(--sky) 100%);
  }

  .cover{position:absolute;overflow:hidden;box-shadow:0 3px 10px rgba(0,0,0,.18)}
  .cover--front{left:110px;top:300px;width:305px;height:430px}
  .cover--back{left:434px;top:300px;width:305px;height:430px}
  .spine{left:110px;top:750px;width:629px;height:120px}

  .front-panel{
    position:absolute;left:0;top:0;width:238px;height:320px;background:var(--paper);
    padding:18px 18px 0 18px;
  }
  .brand{display:flex;align-items:center;gap:6px;font-weight:600;font-size:10px;color:var(--ink);letter-spacing:.2px}
  .brand__mark{width:12px;height:12px;background:var(--teal);flex:none}
  .brand--boxed{background:var(--paper);padding:6px 8px;display:inline-flex}

  .year{margin-top:70px;font-weight:800;font-size:58px;line-height:.9;color:var(--ink);letter-spacing:-1px}
  .district{margin-top:8px;font-weight:800;font-size:25px;line-height:1;color:var(--ink)}
  .district__sub{font-weight:600;font-size:15px;line-height:1.2;letter-spacing:.5px}
  .rule{margin:16px 0 10px;height:2px;width:100%;background:var(--ink)}
  .report{font-weight:300;font-size:12px;letter-spacing:.6px;color:var(--ink-soft)}
  .report__title{font-weight:800;font-size:22px;letter-spacing:.3px;color:var(--ink)}

  .back-card{
    position:absolute;left:110px;top:285px;width:110px;height:90px;background:var(--paper);padding:10px;
  }
  .back-card .brand{font-size:8px}
  .back-card .brand__mark{width:9px;height:9px}
  .address{margin-top:8px;font-size:6px;line-height:1.45;color:var(--ink-soft)}

  .spine__content{
    position:absolute;inset:0;display:flex;flex-direction:column;align-items:center;justify-content:center;gap:2px;
  }
  .spine__district{font-weight:800;font-size:17px;letter-spacing:.5px;color:var(--paper);text-shadow:0 1px 2px rgba(0,0,0,.25)}
  .spine__report{font-weight:400;font-size:13px;letter-spacing:1px;color:var(--paper);text-shadow:0 1px 2px rgba(0,0,0,.25)}
  .spine .brand{position:absolute;left:14px;top:14px;font-size:8px}
  .spine .brand__mark{width:9px;height:9px}
</style>
</head>
<body>

  <section class="cover cover--front" aria-label="Front cover">
    <div class="pattern" role="img" aria-label="Colourful interlocking geometric block pattern in teal, mint, yellow, coral and peach"></div>
    <div class="front-panel">
      <div class="brand"><span class="brand__mark"></span>Brightpath Learning, LLC</div>
      <div class="year">2020</div>
      <div class="district">LINDEN<br><span class="district__sub">SCHOOL DISTRICT</span></div>
      <div class="rule"></div>
      <div class="report">COMPREHENSIVE NEEDS</div>
      <div class="report__title">ASSESSMENT</div>
    </div>
  </section>

  <section class="cover cover--back" aria-label="Back cover">
    <div class="pattern" role="img" aria-label="Colourful interlocking geometric block pattern in teal, mint, yellow, coral and peach"></div>
    <div class="back-card">
      <div class="brand"><span class="brand__mark"></span>Brightpath Learning</div>
      <p class="address">1200 Harbor Lane, Suite 4<br>Fairview, OR 97000<br>555-0142</p>
    </div>
  </section>

  <section class="cover spine" aria-label="Spine">
    <div class="pattern" role="img" aria-label="Colourful interlocking geometric block pattern in teal, mint, yellow, coral and peach"></div>
    <div class="brand brand--boxed"><span class="brand__mark"></span>Brightpath Learning</div>
    <div class="spine__content">
      <div class="spine__district">LINDEN COUNTY SCHOOL DISTRICT</div>
      <div class="spine__report">COMPREHENSIVE NEEDS ASSESSMENT</div>
    </div>
  </section>

</body>
</html>
```